Brindle Advisory Business Card Design

Business card for business consulting company, using attached logo. We do financial and strategic consulting, and want a clean, professional image with a bit of fun. Our logo is a flat whale tail, which symbolizes the Orca whale, a highly collaborative, group based animal that is very successful in navigating the ocean, protecting the herd, and hunting. We like the logo that is blue and gray on white one one side, but would be open to a blue card with white lettering on the other side... or whatever you'd suggest
Updates
Hi all - I have had the logo modified to take the shadowing off the tail. I will post it on the brief... under a file name called updated logo. thank you Added Saturday, April 25, 2015
Target Market(s)
Small to medium sized businesses ($10M to $500M in revenue per year), financial and sales executives, general managers, attorneys and CPAs
Industry/Entity Type
Financial
Contact Information for Business Card
Want company name, contact info - name, title, telephone, email, website, linkedin, twitter and Facebook. No physical address yet.
Requirements
Must have
- contemporary design, bold, strong, confident but with a bit of fun. prominently feature the logo and the whale tail icon
Nice to have
- unique touches that would differentiate us from a regular card... for example, logo and writing all on front on white background, but on back - logo in white on a blue background
- open to idea of different shapes of card than standard... but not sure
Should not have
- ?

```html
<!DOCTYPE html>
<html lang="en">
<head>
<meta charset="utf-8">
<title>Brindle Advisory – Business Card</title>
<link href="https://fonts.googleapis.com/css2?family=Open+Sans:wght@400;600;700&display=swap" rel="stylesheet">
<style>
  :root{
    --stage:#1c1a1b;
    --card-dark:#231f20;
    --card-light:#ffffff;
    --brand-blue:#0a56a0;
    --brand-gray:#a7a9ac;
    --white:#ffffff;
  }
  *{margin:0;padding:0;box-sizing:border-box}
  html,body{width:1200px;height:960px;overflow:hidden;background:var(--stage)}
  body{position:relative;font-family:"Open Sans",Arial,sans-serif}

  .card{position:absolute;width:535px;height:298px}
  .card--front-dark{left:53px;top:165px;background:var(--card-dark)}
  .card--front-light{left:614px;top:165px;background:var(--card-light)}
  .card--back-dark{left:53px;top:497px;background:var(--card-dark)}
  .card--back-blue{left:614px;top:497px;background:var(--brand-blue)}

  /* logo lockup */
  .lockup{position:absolute;display:flex;align-items:center}
  .lockup__mark{flex:none;border-radius:4px;background:var(--brand-blue)}
  .lockup__words{display:flex;flex-direction:column;align-items:flex-end}
  .lockup__name{font-weight:600;letter-spacing:-0.5px;line-height:1;white-space:nowrap}
  .lockup__tag{color:var(--brand-blue);line-height:1;white-space:nowrap}

  .lockup--small{left:51px;top:131px}
  .lockup--small .lockup__mark{width:33px;height:33px;margin-right:5px}
  .lockup--small .lockup__name{font-size:21px}
  .lockup--small .lockup__tag{font-size:7px;margin-top:1px}

  .lockup--large{left:69px;top:117px}
  .lockup--large .lockup__mark{width:66px;height:66px;margin-right:8px;border-radius:6px}
  .lockup--large .lockup__name{font-size:42px}
  .lockup--large .lockup__tag{font-size:14px;margin-top:2px}

  .card--front-dark .lockup__name,
  .card--back-dark .lockup__name{color:var(--brand-gray)}
  .card--front-light .lockup__name{color:var(--brand-blue)}
  .card--back-blue .lockup__mark{background:var(--white)}
  .card--back-blue .lockup__name,
  .card--back-blue .lockup__tag{color:var(--white)}

  /* contact block */
  .contact{position:absolute;left:301px;top:70px;color:var(--brand-blue)}
  .contact__name{font-size:15px;line-height:1.2}
  .contact__title{font-size:10px;font-weight:700;margin-bottom:13px}
  .contact__row{display:flex;align-items:center;height:22px;font-size:12px}
  .contact__icon{width:16px;height:16px;margin:0 8px 0 1px;flex:none}
  .social{display:flex;flex-direction:column;gap:7px;margin-top:20px;margin-left:4px}
  .social__dot{width:11px;height:11px;border-radius:50%;background:var(--brand-blue)}
</style>
</head>
<body>

  <!-- Front, dark -->
  <section class="card card--front-dark">
    <div class="lockup lockup--small">
      <span class="lockup__mark"></span>
      <div class="lockup__words">
        <span class="lockup__name">Brindle Advisory</span>
        <span class="lockup__tag">business consulting</span>
      </div>
    </div>
    <div class="contact">
      <p class="contact__name">Brindle</p>
      <p class="contact__title">business consulting</p>
      <div class="contact__row">
        <svg class="contact__icon" viewBox="0 0 16 16"><circle cx="8" cy="8" r="8" fill="var(--brand-blue)"/><path d="M5 4.5c.6-.5 1.2-.3 1.5.2l.7 1.3c.2.4 0 .8-.3 1l-.5.3c.4 1 1.2 1.8 2.2 2.2l.3-.5c.2-.3.6-.5 1-.3l1.3.7c.5.3.7.9.2 1.5-1.2 1.2-3.4.3-5-1.3S3.8 5.7 5 4.5z" fill="var(--card-dark)"/></svg>
        000-000 000
      </div>
      <div class="contact__row">
        <svg class="contact__icon" viewBox="0 0 16 16"><circle cx="8" cy="8" r="8" fill="var(--brand-blue)"/><rect x="4.5" y="6" width="7" height="5" rx="1" fill="var(--card-dark)"/><rect x="6" y="4" width="4" height="2.5" fill="var(--card-dark)"/></svg>
        000-000 000
      </div>
      <div class="contact__row">
        <svg class="contact__icon" viewBox="0 0 16 16"><circle cx="8" cy="8" r="8" fill="var(--brand-blue)"/><rect x="4" y="5" width="8" height="6" fill="none" stroke="var(--card-dark)" stroke-width="1.2"/><path d="M4 5l4 3.5L12 5" fill="none" stroke="var(--card-dark)" stroke-width="1.2"/></svg>
        brindleadvisory@.com
      </div>
      <div class="contact__row">
        <svg class="contact__icon" viewBox="0 0 16 16"><circle cx="8" cy="8" r="8" fill="var(--brand-blue)"/><circle cx="8" cy="8" r="4" fill="none" stroke="var(--card-dark)" stroke-width="1.1"/><path d="M4 8h8M8 4c-1.5 2.5-1.5 5.5 0 8M8 4c1.5 2.5 1.5 5.5 0 8" fill="none" stroke="var(--card-dark)" stroke-width=".9"/></svg>
        brindleadvisory.com
      </div>
      <div class="social">
        <span class="social__dot"></span><span class="social__dot"></span><span class="social__dot"></span>
      </div>
    </div>
  </section>

  <!-- Front, light -->
  <section class="card card--front-light">
    <div class="lockup lockup--small">
      <span class="lockup__mark"></span>
      <div class="lockup__words">
        <span class="lockup__name">Brindle Advisory</span>
        <span class="lockup__tag">business consulting</span>
      </div>
    </div>
    <div class="contact">
      <p class="contact__name">Brindle</p>
      <p class="contact__title">business consulting</p>
      <div class="contact__row">
        <svg class="contact__icon" viewBox="0 0 16 16"><circle cx="8" cy="8" r="8" fill="var(--brand-blue)"/><path d="M5 4.5c.6-.5 1.2-.3 1.5.2l.7 1.3c.2.4 0 .8-.3 1l-.5.3c.4 1 1.2 1.8 2.2 2.2l.3-.5c.2-.3.6-.5 1-.3l1.3.7c.5.3.7.9.2 1.5-1.2 1.2-3.4.3-5-1.3S3.8 5.7 5 4.5z" fill="var(--white)"/></svg>
        000-000 000
      </div>
      <div class="contact__row">
        <svg class="contact__icon" viewBox="0 0 16 16"><circle cx="8" cy="8" r="8" fill="var(--brand-blue)"/><rect x="4.5" y="6" width="7" height="5" rx="1" fill="var(--white)"/><rect x="6" y="4" width="4" height="2.5" fill="var(--white)"/></svg>
        000-000 000
      </div>
      <div class="contact__row">
        <svg class="contact__icon" viewBox="0 0 16 16"><circle cx="8" cy="8" r="8" fill="var(--brand-blue)"/><rect x="4" y="5" width="8" height="6" fill="none" stroke="var(--white)" stroke-width="1.2"/><path d="M4 5l4 3.5L12 5" fill="none" stroke="var(--white)" stroke-width="1.2"/></svg>
        brindleadvisory@.com
      </div>
      <div class="contact__row">
        <svg class="contact__icon" viewBox="0 0 16 16"><circle cx="8" cy="8" r="8" fill="var(--brand-blue)"/><circle cx="8" cy="8" r="4" fill="none" stroke="var(--white)" stroke-width="1.1"/><path d="M4 8h8M8 4c-1.5 2.5-1.5 5.5 0 8M8 4c1.5 2.5 1.5 5.5 0 8" fill="none" stroke="var(--white)" stroke-width=".9"/></svg>
        brindleadvisory.com
      </div>
      <div class="social">
        <span class="social__dot"></span><span class="social__dot"></span><span class="social__dot"></span>
      </div>
    </div>
  </section>

  <!-- Back, dark -->
  <section class="card card--back-dark">
    <div class="lockup lockup--large">
      <span class="lockup__mark"></span>
      <div class="lockup__words">
        <span class="lockup__name">Brindle Advisory</span>
        <span class="lockup__tag">business consulting</span>
      </div>
    </div>
  </section>

  <!-- Back, blue -->
  <section class="card card--back-blue">
    <div class="lockup lockup--large">
      <span class="lockup__mark"></span>
      <div class="lockup__words">
        <span class="lockup__name">Brindle Advisory</span>
        <span class="lockup__tag">business consulting</span>
      </div>
    </div>
  </section>

</body>
</html>
```